Super Cool Postcard Needed - design for animal chiropractor!

I need a postcard that will grab peoples attention for them to have their animal (dog,cat, horse) adjusted. I would prefer two sided post card - not to be mailed but to be handed out. The postcard needs to give them the info on why their pet would need to be adjusted. I included in the documents - photos, a flier and info on what animal chiropractic is. I would say to focus the flier on small animal but include horses (horse community is very familiar with chiropractic).

Target Market(s)

animal owners interested in wellness/holistic care for their pet

Font styles to use
Sans Serif

Colors

Designer to choose colors to be used in the design.

Requirements
Must have
• Logo, contact info, info on why a pet needs chiropractic, front and back design - not meant for mailing
Nice to have
• pictures
Should not have
• an area for an address

```html
<!DOCTYPE html>
<html lang="en">
<head>
<meta charset="utf-8">
<title>Chiropractic Care for Your Pet – Handout Postcard</title>
<link rel="stylesheet" href="https://fonts.googleapis.com/css2?family=Montserrat:wght@600;700;800&family=Roboto+Condensed:wght@400;700&display=swap">
<style>
  :root {
    --red: #e5202a;
    --black: #0b0b0b;
    --ink: #1c1c1c;
    --white: #ffffff;
    --grey-bg: #e4e4e4;
    --paper: #ececec;
    --yellow: #f4d21a;
    --photo-warm: #8a7a6a;
  }
  * { box-sizing: border-box; margin: 0; padding: 0; }
  html, body { width: 1200px; height: 1000px; overflow: hidden; }
  body {
    background: var(--grey-bg);
    position: relative;
    font-family: "Roboto Condensed", "Arial Narrow", sans-serif;
  }

  /* ---------- Front side ---------- */
  .card-front {
    position: absolute; left: 39px; top: 35px;
    width: 590px; height: 456px;
    background: var(--black); color: var(--white);
    overflow: hidden;
    box-shadow: 0 8px 14px rgba(0,0,0,.35);
  }
  .corner { position: absolute; }
  .corner-top { left: 0; top: 0; }
  .corner-bottom { right: 0; bottom: 0; }

  .portrait-ring {
    position: absolute; left: 22px; top: 34px;
    width: 230px; height: 230px; border-radius: 50%;
    border: 2px solid var(--red);
  }
  .portrait {
    position: absolute; left: 30px; top: 42px;
    width: 214px; height: 214px; border-radius: 50%;
    background: radial-gradient(circle at 50% 45%, #b9a690 0%, #8b8580 45%, #5a5f66 100%);
  }
  .intro-banner {
    position: absolute; left: 0; top: 262px;
    width: 290px; height: 34px;
    background: var(--red);
    border-radius: 0 18px 18px 0;
    padding: 3px 10px 0 24px;
    font-size: 11.5px; line-height: 14px;
  }
  .intro-banner em { font-style: normal; color: var(--yellow); }

  .front-title {
    position: absolute; left: 262px; top: 30px; width: 320px;
    text-align: center;
    font-family: "Montserrat", sans-serif; line-height: 1;
  }
  .front-title .line-1 { font-size: 22px; font-weight: 700; letter-spacing: .3px; }
  .front-title .line-2 { font-size: 33px; font-weight: 800; color: var(--red); margin-top: 2px; }

  .benefits {
    position: absolute; left: 303px; top: 96px; width: 270px;
    font-size: 11px; line-height: 14.5px;
  }
  .benefits-lead { font-weight: 700; font-size: 12px; line-height: 13px; }
  .benefits ul { list-style: none; }
  .benefits li { position: relative; padding-left: 10px; }
  .benefits li::before {
    content: "✓"; position: absolute; left: 0; top: 0;
    color: var(--red); font-weight: 700; font-size: 10px;
  }

  .brand {
    position: absolute; text-align: center;
    font-family: "Montserrat", sans-serif; font-weight: 700; color: var(--white);
  }
  .brand-mark { display: block; margin: 0 auto; border-radius: 50%; background: var(--red); }
  .brand-front { left: 18px; top: 340px; width: 110px; font-size: 10px; }
  .brand-front .brand-mark { width: 50px; height: 50px; margin-bottom: 8px; }

  .contact-front { position: absolute; left: 134px; top: 354px; width: 170px; }
  .contact-note { font-size: 10.5px; line-height: 12px; }
  .phone { font-family: "Montserrat", sans-serif; font-weight: 700; }
  .contact-front .phone { font-size: 16px; margin-top: 12px; }
  .web { font-weight: 700; font-size: 8.3px; }

  .front-note {
    position: absolute; left: 303px; top: 344px; width: 260px;
    font-size: 11px; line-height: 14.5px; text-align: justify;
  }

  /* ---------- Back side ---------- */
  .card-back {
    position: absolute; left: 569px; top: 507px;
    width: 584px; height: 451px;
    background: var(--paper); color: var(--ink);
    overflow: hidden;
    box-shadow: 0 8px 14px rgba(0,0,0,.35);
  }
  .back-photo-faded {
    position: absolute; left: 0; top: 103px; width: 376px; height: 348px;
    background: linear-gradient(135deg, #e6e6e6 0%, #c9c9c9 45%, #b5b5b5 75%, #d8d8d8 100%);
  }
  .intro-block {
    position: absolute; left: 0; top: 0; width: 376px; height: 103px;
    background: var(--black); color: var(--white);
    padding: 19px 10px 0 22px;
    font-size: 8px; line-height: 11.5px;
  }
  .section-head {
    font-family: "Roboto Condensed", sans-serif; font-weight: 700;
    color: var(--red); font-size: 9px; text-transform: uppercase;
  }
  .back-content {
    position: absolute; left: 22px; top: 112px; width: 350px;
    font-size: 8.1px; line-height: 13.2px;
  }
  .back-content ul { list-style: none; margin-bottom: 8px; }
  .back-content li { position: relative; padding-left: 7px; }
  .back-content li::before {
    content: ""; position: absolute; left: 0; top: 4px;
    width: 4px; height: 4px; background: var(--red);
  }
  .back-content li.plain::before { display: none; }
  .age-line { margin-bottom: 10px; }

  .side-column {
    position: absolute; left: 378px; top: 0; width: 206px; height: 451px;
    background: var(--black); color: var(--white);
  }
  .horse-photo {
    position: absolute; left: 8px; top: 18px; width: 178px; height: 235px;
    background: linear-gradient(180deg, #6f9bd0 0%, #9bbbd9 35%, #5f6e45 55%, #8a7358 80%, #6d5a45 100%);
  }
  .brand-back { left: 0; top: 268px; width: 206px; font-size: 12px; }
  .brand-back .brand-mark { width: 82px; height: 82px; margin-bottom: 18px; }
  .brand-back .phone { font-size: 20px; margin-top: 6px; }
  .brand-back .web { font-family: "Roboto Condensed", sans-serif; font-size: 8.5px; }
</style>
</head>
<body>

<section class="card-front">
  <svg class="corner corner-top" width="78" height="78" viewBox="0 0 78 78"><polygon points="0,0 78,0 0,78" fill="#e5202a"/></svg>
  <svg class="corner corner-bottom" width="48" height="70" viewBox="0 0 48 70"><polygon points="48,0 48,70 0,70" fill="#e5202a"/></svg>

  <div class="portrait-ring"></div>
  <div class="portrait" role="img" aria-label="Photo of the chiropractor smiling while holding a black puppy in her clinic"></div>
  <p class="intro-banner">Introducing <em>Dr. Laura Bennett</em>, chiropractor, who has been providing chiropractic care for over <em>15 years!</em></p>

  <h1 class="front-title">
    <span class="line-1">CHIROPRACTIC CARE</span><br>
    <span class="line-2">FOR YOUR PET!</span>
  </h1>

  <div class="benefits">
    <p class="benefits-lead">Your dog or cat can benefit from Chiropractic adjustments if they:</p>
    <ul>
      <li>Have a limp that will not go away</li>
      <li>Do not want to jump in, out or on things as much or anymore</li>
      <li>Yelps with certain activities</li>
      <li>Are slow getting up or laying down</li>
      <li>Have been diagnosed with disc disease</li>
      <li>Wellness - prevention - a well moving spine will help prevent arthritis later in life</li>
      <li>They are in rehab from a current injury - sprain/strain, surgery</li>
      <li>Are involved in athletics - flyball, agility - top athletes receive regular chiropractic care</li>
      <li>Are working dogs - pulling wheelchairs, police dogs</li>
    </ul>
  </div>

  <div class="brand brand-front">
    <span class="brand-mark"></span>
    DR. LAURA BENNETT
  </div>

  <div class="contact-front">
    <p class="contact-note">To schedule an appointment<br>or for more information,<br>contact us at</p>
    <p class="phone">555- 014-2290</p>
    <p class="web">www.drlaurabennett.com/animal-chiropractic</p>
  </div>

  <p class="front-note">Animal chiropractic adjustments are not only for pets with injuries, it's great to start young so that we know how the spine/extremities are moving prior to a problem. Chiropractic adjustments definitely help with new and existing injuries. We also offer low level laser treatments to assist in the healing process.</p>
</section>

<section class="card-back">
  <div class="back-photo-faded" role="img" aria-label="Faded photo of a dog being adjusted on a wooden floor"></div>

  <div class="intro-block">
    <p class="section-head">What is chiropractic ?</p>
    <p>What is chiropractic - in simplest terms, a conservative approach to healthcare. We focus on the movement in the joints (spine/extremities) for the overall health and wellness of the pet. Restrictions in joint motion, can affect such things as athletic performance, normal biomechanics leading to repetitive stress injuries and sprain/strains. The issue, most restrictions in joint motions are subclinical and go undetected until they manifest into a problem.</p>
  </div>

  <div class="back-content">
    <p class="section-head">Classic things chiropractic will help an animal with:</p>
    <ul>
      <li>post surgical (addressing compensatory gaits of (ex) TPLO surgeries)</li>
      <li>ambiguous limp, diagnostics come up clean</li>
      <li>dogs that have stopped jumping up on the couch or in and out of the car perhaps have fixations in the lower back or pelvis</li>
      <li>offers an alternative for treating acute and chronic musculoskeletal injuries without drugs</li>
      <li>senior pets moving better</li>
      <li>athletes - fly ball, agility, working</li>
      <li>working dogs - pulling, pushing, jumping</li>
      <li>wellness - prevention making sure joints are moving well to prevent arthritis</li>
      <li>pregnancy - helping the birthing process so the pelvis can move</li>
      <li>every test has been run, nothing seems to be helping the pet - send the hail mary pass</li>
    </ul>
    <p class="age-line"><span class="section-head">Age:</span> Age of pet - never too young or too old, puppies/kittens - seniors</p>
    <p class="section-head">Some signs/symptoms owners will report:</p>
    <ul>
      <li>Yelping in pain after a sudden movement when no other symptoms are present</li>
      <li class="plain">Weak front legs with no site of pain</li>
      <li>Looking, yelping or biting when being picked up around the chest area</li>
      <li>Hunched back</li>
      <li>Muscle spasms along the back</li>
      <li>Hip pain in the hind legs with no sign of canine arthritis</li>
      <li>Trouble standing or laying down</li>
      <li>Inability to jump</li>
      <li>Not wanting to perform normal work - i.e. pulling a wheel chair</li>
    </ul>
  </div>

  <aside class="side-column">
    <div class="horse-photo" role="img" aria-label="Photo of the chiropractor adjusting a horse outdoors under a tree"></div>
    <div class="brand brand-back">
      <span class="brand-mark"></span>
      DR. LAURA BENNETT
      <p class="phone">555- 014-2290</p>
      <p class="web">www.drlaurabennett.com/animal-chiropractic</p>
    </div>
  </aside>
</section>

</body>
</html>
```